Poster design for a company operating care homes in the UK showcasing our core values

We need a poster to display in our care homes showcasing our new core values:

Purpose
We are driven by a clear understanding of why we do what we do: to enrich lives, honour legacies and make a meaningful difference every day, for our residents, their families, our colleagues and our community.

Excellence
We hold ourselves to the highest standards, delivering exceptional care and creating an environment where both residents and staff can thrive.

Openness
We build trust through honest, respectful communication, welcoming feedback, sharing ideas, and embracing change as a path to continuous growth.

Passion
We are passionate about delivering exceptional care. We take pride in what we do and in making a real difference in people’s lives.

Learning
We are committed to personal and professional growth; empowering each other through ongoing development, reflection, and shared knowledge.

Empathy
We actively listen and seek to understand before being understood, recognising the unique stories, feelings, and needs of others.

I have attached a small graphic that we would like you try to incorporate, in addition to our company logo. Please theme the rest of the poster around our company colours.

```html
<!DOCTYPE html>
<html lang="en">
<head>
<meta charset="utf-8">
<title>Ashcroft – Core Values Posters</title>
<link rel="stylesheet" href="https://fonts.googleapis.com/css2?family=Poppins:wght@400;500;800&display=swap">
<style>
  :root {
    --navy: #3a5170;
    --peach: #eea883;
    --paper: #fdfdfd;
    --white: #ffffff;
    --sheet: #ffffff;
  }
  * { box-sizing: border-box; margin: 0; padding: 0; }
  html, body {
    width: 931px; height: 1200px; overflow: hidden;
    background: var(--sheet);
    font-family: "Poppins", sans-serif;
  }
  .board { position: relative; width: 931px; height: 1200px; }

  .poster {
    position: absolute;
    width: 334px; height: 540px;
    background: var(--white);
    padding: 8px 8px 9px 7px;
    box-shadow: 3px 3px 4px rgba(0,0,0,0.35);
  }
  .poster--peach-on-navy { left: 110px; top: 50px; }
  .poster--navy-on-white { left: 513px; top: 50px; }
  .poster--mixed { left: 277px; top: 622px; }

  .poster__header {
    height: 46px;
    display: flex; align-items: center; justify-content: center;
    gap: 11px;
    color: var(--white);
  }
  .header--navy { background: var(--navy); }
  .header--peach { background: var(--peach); }

  .brand {
    display: flex; align-items: center; gap: 5px;
    font-weight: 500; font-size: 14px; letter-spacing: 0.5px;
  }
  .brand__mark { width: 12px; height: 12px; background: currentColor; }
  .poster__divider { width: 1px; height: 22px; background: currentColor; }
  .poster__heading { font-weight: 400; font-size: 15.5px; letter-spacing: 0.2px; }

  .values {
    display: grid;
    grid-template-columns: 1fr 1fr;
    grid-template-rows: repeat(3, 159px);
  }
  .value {
    display: flex; flex-direction: column; align-items: center;
    text-align: center;
    padding: 8px 6px 14px;
  }
  .value__name {
    font-weight: 800; font-size: 20.5px; line-height: 1.2;
    letter-spacing: 0.3px;
  }
  .value__text {
    flex: 1;
    display: flex; align-items: center;
    font-size: 8.3px; line-height: 11.1px; font-weight: 500;
  }
  .value--top .value__text { align-items: flex-start; margin-top: 4px; }
  .value--top { padding-bottom: 4px; }

  .tone--peach-navy { background: var(--peach); color: var(--navy); }
  .tone--navy-peach { background: var(--navy); color: var(--peach); }
  .tone--navy-white { background: var(--navy); color: var(--white); }
  .tone--paper-navy { background: var(--paper); color: var(--navy); }
  .tone--peach-white { background: var(--peach); color: var(--white); }
</style>
</head>
<body>
<main class="board">

  <!-- Variant: peach and navy chequer -->
  <article class="poster poster--peach-on-navy">
    <header class="poster__header header--navy">
      <div class="brand"><span class="brand__mark"></span>ASHCROFT</div>
      <span class="poster__divider"></span>
      <h1 class="poster__heading">our new core values:</h1>
    </header>
    <section class="values">
      <div class="value value--top tone--peach-navy">
        <h2 class="value__name">PURPOSE</h2>
        <p class="value__text">We are driven by a<br>clear understanding<br>of why we do what we do:<br>to enrich lives,<br>honour legacies and<br>make a meaningful difference<br>every day, for our residents,<br>their families,<br>our colleagues and<br>our community.</p>
      </div>
      <div class="value tone--navy-peach">
        <h2 class="value__name">EXCELLENCE</h2>
        <p class="value__text">We hold ourselves to the<br>highest standards,<br>delivering exceptional care<br>and creating an environment<br>where both residents<br>and staff can thrive.</p>
      </div>
      <div class="value tone--navy-peach">
        <h2 class="value__name">OPENNESS</h2>
        <p class="value__text">We build trust through honest,<br>respectful communication,<br>welcoming feedback,<br>sharing ideas,<br>and embracing change as a<br>path to continuous growth.</p>
      </div>
      <div class="value tone--peach-navy">
        <h2 class="value__name">PASSION</h2>
        <p class="value__text">We are passionate about<br>delivering exceptional care.<br>We take pride in what we do<br>and in making a real difference<br>in people’s lives.</p>
      </div>
      <div class="value tone--peach-navy">
        <h2 class="value__name">LEARNING</h2>
        <p class="value__text">We are committed to personal<br>and professional growth;<br>empowering each other through<br>ongoing development,<br>reflection, and shared<br>knowledge.</p>
      </div>
      <div class="value tone--navy-peach">
        <h2 class="value__name">EMPATHY</h2>
        <p class="value__text">We actively listen and seek to<br>understand before<br>being understood,<br>recognising the unique stories,<br>feelings, and needs of others.</p>
      </div>
    </section>
  </article>

  <!-- Variant: navy and white chequer -->
  <article class="poster poster--navy-on-white">
    <header class="poster__header header--navy">
      <div class="brand"><span class="brand__mark"></span>ASHCROFT</div>
      <span class="poster__divider"></span>
      <h1 class="poster__heading">our new core values:</h1>
    </header>
    <section class="values">
      <div class="value value--top tone--paper-navy">
        <h2 class="value__name">PURPOSE</h2>
        <p class="value__text">We are driven by a<br>clear understanding<br>of why we do what we do:<br>to enrich lives,<br>honour legacies and<br>make a meaningful difference<br>every day, for our residents,<br>their families,<br>our colleagues and<br>our community.</p>
      </div>
      <div class="value tone--navy-white">
        <h2 class="value__name">EXCELLENCE</h2>
        <p class="value__text">We hold ourselves to the<br>highest standards,<br>delivering exceptional care<br>and creating an environment<br>where both residents<br>and staff can thrive.</p>
      </div>
      <div class="value tone--navy-white">
        <h2 class="value__name">OPENNESS</h2>
        <p class="value__text">We build trust through honest,<br>respectful communication,<br>welcoming feedback,<br>sharing ideas,<br>and embracing change as a<br>path to continuous growth.</p>
      </div>
      <div class="value tone--paper-navy">
        <h2 class="value__name">PASSION</h2>
        <p class="value__text">We are passionate about<br>delivering exceptional care.<br>We take pride in what we do<br>and in making a real difference<br>in people’s lives.</p>
      </div>
      <div class="value tone--paper-navy">
        <h2 class="value__name">LEARNING</h2>
        <p class="value__text">We are committed to personal<br>and professional growth;<br>empowering each other through<br>ongoing development,<br>reflection, and shared<br>knowledge.</p>
      </div>
      <div class="value tone--navy-white">
        <h2 class="value__name">EMPATHY</h2>
        <p class="value__text">We actively listen and seek to<br>understand before<br>being understood,<br>recognising the unique stories,<br>feelings, and needs of others.</p>
      </div>
    </section>
  </article>

  <!-- Variant: peach header with mixed tiles -->
  <article class="poster poster--mixed">
    <header class="poster__header header--peach">
      <div class="brand"><span class="brand__mark"></span>ASHCROFT</div>
      <span class="poster__divider"></span>
      <h1 class="poster__heading">our new core values:</h1>
    </header>
    <section class="values">
      <div class="value value--top tone--paper-navy">
        <h2 class="value__name">PURPOSE</h2>
        <p class="value__text">We are driven by a<br>clear understanding<br>of why we do what we do:<br>to enrich lives,<br>honour legacies and<br>make a meaningful difference<br>every day, for our residents,<br>their families,<br>our colleagues and<br>our community.</p>
      </div>
      <div class="value tone--peach-white">
        <h2 class="value__name">EXCELLENCE</h2>
        <p class="value__text">We hold ourselves to the<br>highest standards,<br>delivering exceptional care<br>and creating an environment<br>where both residents<br>and staff can thrive.</p>
      </div>
      <div class="value tone--navy-white">
        <h2 class="value__name">OPENNESS</h2>
        <p class="value__text">We build trust through honest,<br>respectful communication,<br>welcoming feedback,<br>sharing ideas,<br>and embracing change as a<br>path to continuous growth.</p>
      </div>
      <div class="value tone--paper-navy">
        <h2 class="value__name">PASSION</h2>
        <p class="value__text">We are passionate about<br>delivering exceptional care.<br>We take pride in what we do<br>and in making a real difference<br>in people’s lives.</p>
      </div>
      <div class="value tone--paper-navy">
        <h2 class="value__name">LEARNING</h2>
        <p class="value__text">We are committed to personal<br>and professional growth;<br>empowering each other through<br>ongoing development,<br>reflection, and shared<br>knowledge.</p>
      </div>
      <div class="value tone--peach-white">
        <h2 class="value__name">EMPATHY</h2>
        <p class="value__text">We actively listen and seek to<br>understand before<br>being understood,<br>recognising the unique stories,<br>feelings, and needs of others.</p>
      </div>
    </section>
  </article>

</main>
</body>
</html>
```